Fitness Company Valentine's Day Special Flyer

We need an 8x10 flyer designed for our Valentine's Day Special Promo offer to the public. We've included the flyer's text and details - please include all information in the word document attached. DO NOT use this as a design template just the information. We expect something awesome!!!
- The flyer MUST be 8x10 in PSD format (CS3 Compatible) INCLUDING ALL Layers and Fonts
- Please include fitness pictures
- Include our Logo (attached)
- ***Please use the color schemes used in our logo to help with the design!!!!
Industry/Entity Type
Fitness
Look and feel
Each slider illustrates characteristics of the customer's brand and the style your logo design should communicate.

```html
<!DOCTYPE html>
<html lang="en">
<head>
<meta charset="utf-8">
<title>Valentine's Day 2-for-1 Special</title>
<link rel="stylesheet" href="https://fonts.googleapis.com/css2?family=Alfa+Slab+One&family=Montserrat:wght@600;700;800&family=Yesteryear&display=swap">
<style>
  :root {
    --red: #ee1c25;
    --deep-red: #c8101a;
    --maroon: #5c1010;
    --plum: #3b1744;
    --yellow: #ffff66;
    --ink: #1c1c1c;
    --white: #ffffff;
    --grey-light: #e6e6e6;
    --grey-mid: #a9a9a9;
  }
  * { box-sizing: border-box; margin: 0; padding: 0; }
  html, body { width: 960px; height: 1200px; overflow: hidden; background: var(--white); }
  .flyer { position: relative; width: 960px; height: 1200px; overflow: hidden; background: var(--white); }

  .title-band {
    position: absolute; left: 14px; top: 0; width: 932px; height: 240px;
    background: var(--red);
    display: flex; flex-direction: column; align-items: center; justify-content: center;
  }
  .title-band h1 {
    font-family: "Alfa Slab One", serif; font-weight: 400;
    color: var(--white); font-size: 84px; line-height: 98px; text-align: center;
    text-shadow: 4px 5px 0 #4a0a0a;
  }

  .tagline {
    position: absolute; left: 0; top: 250px; width: 960px; text-align: center;
    font-family: "Yesteryear", cursive; color: var(--plum);
    font-size: 50px; line-height: 56px;
  }

  .benefits {
    position: absolute; left: 0; top: 372px; width: 960px; height: 76px;
    background: var(--maroon); color: var(--white);
    font-family: "Montserrat", sans-serif; font-weight: 600; font-size: 42px;
    display: flex; align-items: center; justify-content: center; gap: 16px;
  }

  .scene { position: absolute; left: 0; top: 448px; width: 960px; height: 752px; }
  .gym-photo {
    position: absolute; left: 0; top: 0; width: 960px; height: 752px;
    background: linear-gradient(160deg, var(--grey-light) 0%, #cfcfcf 45%, var(--grey-mid) 100%);
  }
  .swoosh { position: absolute; left: 0; top: 0; }
  .couple-photo {
    position: absolute; left: 500px; top: 120px; width: 460px; height: 632px;
    background: linear-gradient(180deg, #e9d3c4 0%, #f3ece8 60%, #f7f4f2 100%);
    border-radius: 220px 0 0 0;
  }
  .balloon {
    position: absolute; left: 594px; top: 368px; width: 326px; height: 300px;
    background: var(--deep-red); border-radius: 140px 140px 160px 160px;
    display: flex; align-items: center; justify-content: center;
  }
  .balloon p {
    font-family: "Montserrat", sans-serif; font-weight: 700; color: var(--white);
    font-size: 29px; line-height: 35px; text-align: center;
  }

  .offer-box {
    position: absolute; left: 66px; top: 454px; width: 498px; height: 240px;
    background: var(--yellow); padding: 8px 10px 0 14px;
    font-family: "Montserrat", sans-serif; font-weight: 600; color: var(--ink);
    font-size: 19px; line-height: 28px; white-space: nowrap;
  }
  .offer-box ul { list-style: none; }
  .offer-box li { padding-left: 14px; text-indent: -14px; }
  .offer-box li::before { content: "•"; margin-right: 4px; }

  .love-line {
    position: absolute; left: 20px; top: 712px; width: 510px; text-align: center;
    font-family: "Alfa Slab One", serif; color: var(--red); font-size: 44px; line-height: 58px;
    white-space: nowrap;
    text-shadow:
      2px 2px 0 var(--white), -2px -2px 0 var(--white), 2px -2px 0 var(--white), -2px 2px 0 var(--white),
      4px 4px 3px rgba(0,0,0,.35);
  }

  .contact {
    position: absolute; left: 32px; width: 520px;
    font-family: "Montserrat", sans-serif; font-weight: 800; color: var(--ink);
    font-size: 17.5px; line-height: 24px; white-space: nowrap;
  }
  .contact.call { top: 854px; }
  .contact.address { top: 920px; }

  .brand-box {
    position: absolute; left: 26px; top: 1006px; width: 440px; height: 164px;
    background: var(--ink); padding: 10px;
  }
  .brand-box .inner {
    width: 100%; height: 100%; background: var(--white);
    display: flex; align-items: center; justify-content: center; gap: 12px;
  }
  .brand-mark { width: 20px; height: 20px; background: var(--red); }
  .brand-name {
    font-family: "Montserrat", sans-serif; font-weight: 800; color: var(--ink);
    font-size: 26px; letter-spacing: 1px; white-space: nowrap;
  }
</style>
</head>
<body>
<main class="flyer">
  <header class="title-band">
    <h1>Valentine’s Day<br>2-FOR-1 Special</h1>
  </header>

  <p class="tagline">Couples that Train Together Stay Together.<br>This Valentine’s Day Train Together!</p>

  <div class="benefits"><span>Move Better</span><span>|</span><span>Look Better</span><span>|</span><span>Feel Better</span></div>

  <section class="scene">
    <div class="gym-photo" role="img" aria-label="Black and white photo of a group fitness class training in a gym"></div>
    <svg class="swoosh" width="960" height="752" viewBox="0 0 960 752" aria-hidden="true">
      <path d="M540 0 H960 V752 H720 C600 560 560 300 620 120 C640 60 600 20 540 0 Z" fill="var(--red)"/>
      <path d="M0 560 C120 600 200 700 240 752 H0 Z" fill="var(--white)" opacity=".55"/>
    </svg>
    <div class="couple-photo" role="img" aria-label="Photo of a smiling young couple embracing"></div>
    <div class="balloon" role="img" aria-label="Red heart-shaped balloon held by the couple">
      <p>2-FOR-1<br>Valentine’s<br>Day Special<br>ONLY $99</p>
    </div>
  </section>

  <div class="offer-box">
    <p>The perfect gift for You and Your Valentine.</p>
    <p>Included In Your 30 Day Jumpstart:</p>
    <ul>
      <li>Success Start Consultation</li>
      <li>12 Group Personal Training Sessions</li>
      <li>Success Manual with Bonus<br>Nutrition Guide</li>
      <li>Unlimited Coaching Support via Private<br>Teamloop Group</li>
    </ul>
  </div>

  <p class="love-line">Love Your Body<br>This Valentine’s Day</p>

  <p class="contact call">Call Us Now at 555-014-2287 to Reserve This Offer!<br>Expires February 14th | Only 20 Spots Available</p>
  <p class="contact address">Pulsewell Bootcamps | 18 Cedar Ave. Unit 7<br>Ridgeview CO 80000 | www.Pulsewellfit.com</p>

  <div class="brand-box">
    <div class="inner">
      <span class="brand-mark"></span>
      <span class="brand-name">PULSEWELL BOOTCAMPS</span>
    </div>
  </div>
</main>
</body>
</html>
```